I need a new business card design for my pharmacy.

I need a business card design. I will include my logo.
The card needs to be readable. I prefer to have my logo on one side along with my website, the other side includes the other information. Please use combination of black, neon green, white, and silver. This needs to catch the eye but yet be clearly visible and legible. Thanks

Industry/Entity Type

Pharmacy

Contact Information for Business Card

It needs to have the following information listed:
Mel's Apothecary Owner/Pharm D.
7134 North Brook Lane
Sioux Falls, SD 57231
Phone 605-318-6207
Fax 605-318-6209
email: mel@melsapothecary-example.com
www.melsapothecary-example.com
Store hours Monday-Friday 8 am- 7 pm
Saturday 8 am- 12 pm
Sunday Closed
Please utilize the colors black, white, and neon green, maybe silver.

Requirements
Must have
• It needs to be easily readable!
Nice to have
• It should catch the eye.
Should not have
• Do not use any other colors except listed: black, neon green, white, & silver.

```html
<!DOCTYPE html>
<html lang="en">
<head>
<meta charset="utf-8">
<title>Mel's Apothecary – Business Card</title>
<link rel="stylesheet" href="https://fonts.googleapis.com/css2?family=Source+Sans+3:wght@400;600&family=Open+Sans:wght@400&family=Montserrat:wght@700&display=swap">
<style>
  :root {
    --ink: #16181a;
    --ink-soft: #232527;
    --green: #8cc63f;
    --white: #ffffff;
    --paper: #f7f7f6;
    --silver: #b0aeaf;
    --text-dark: #1d1d1d;
  }
  * { margin: 0; padding: 0; box-sizing: border-box; }
  html, body {
    width: 1200px; height: 1200px; overflow: hidden;
    background: var(--silver);
    font-family: "Source Sans 3", sans-serif;
  }
  .card {
    position: absolute;
    width: 712px; height: 418px;
    border-radius: 22px;
    overflow: hidden;
  }

  /* Front */
  .card-front { left: 238px; top: 118px; background: var(--ink); }
  .front-name {
    position: absolute; left: 0; right: 0; top: 166px;
    text-align: center; color: var(--white);
    font-weight: 600; font-size: 52px; letter-spacing: -1px;
  }
  .front-web {
    position: absolute; left: 0; right: 0; top: 280px;
    text-align: center; color: var(--white);
    font-family: "Open Sans", sans-serif; font-size: 16px; letter-spacing: 3px;
  }
  .front-web .accent { color: var(--green); font-weight: 600; }
  .hours-band {
    position: absolute; left: 0; right: 0; bottom: 0; height: 76px;
    background: var(--green); text-align: center; color: var(--text-dark);
  }
  .hours-title {
    margin-top: 10px;
    font-family: "Montserrat", sans-serif; font-weight: 700; font-size: 16px; letter-spacing: .5px;
  }
  .hours-list {
    margin-top: 3px;
    font-family: "Open Sans", sans-serif; font-size: 18px;
  }
  .hours-list .sep { margin: 0 6px; }

  /* Back */
  .card-back { left: 231px; top: 644px; background: var(--paper); }
  .back-wave { position: absolute; left: 0; top: 0; }
  .back-name {
    position: absolute; right: 38px; top: 42px;
    color: var(--white); font-weight: 600; font-size: 31px; letter-spacing: -.5px;
  }
  .back-title {
    position: absolute; right: 38px; top: 87px;
    color: var(--white); font-family: "Open Sans", sans-serif; font-size: 15px;
  }
  .contact-list {
    position: absolute; left: 41px; top: 116px; list-style: none;
    font-family: "Open Sans", sans-serif; font-size: 18px; color: var(--text-dark);
  }
  .contact-list li { display: flex; align-items: center; height: 26.5px; }
  .contact-list svg { width: 16px; height: 16px; margin-right: 20px; fill: var(--green); }
  .contact-address { margin-top: 4px; }
  .lockup {
    position: absolute; left: 41px; top: 294px;
    display: flex; align-items: center; height: 88px;
  }
  .lockup-dot { width: 42px; height: 42px; border-radius: 50%; background: var(--green); }
  .lockup-rule { width: 2px; height: 88px; background: var(--ink); margin: 0 24px 0 88px; }
  .lockup-name { font-weight: 600; font-size: 44px; letter-spacing: -1px; color: var(--ink); }
</style>
</head>
<body>

<section class="card card-front">
  <div class="front-name">Mel's Apothecary</div>
  <div class="front-web">www.<span class="accent">melsapothecary-example</span>.com</div>
  <div class="hours-band">
    <div class="hours-title">STORE HOURS</div>
    <div class="hours-list">Monday-Friday 8 am- 7 pm<span class="sep">|</span>Saturday 8 am- 12 pm<span class="sep">|</span>Sunday Closed</div>
  </div>
</section>

<section class="card card-back">
  <svg class="back-wave" width="712" height="200" viewBox="0 0 712 200">
    <path d="M0,0 H712 V182 C620,180 540,150 450,92 C340,22 160,8 0,38 Z" fill="var(--ink)"/>
    <path d="M0,38 C160,8 340,22 450,92 C540,150 620,180 712,182 V190 C620,188 540,160 448,102 C340,36 170,28 0,48 Z" fill="var(--paper)"/>
    <path d="M60,60 C200,20 360,30 460,100 C545,155 625,182 712,186 V192 C620,190 540,166 455,112 C360,48 210,42 60,60 Z" fill="var(--green)"/>
    <path d="M0,44 C130,12 300,10 400,62 C290,30 150,32 0,58 Z" fill="var(--green)"/>
  </svg>

  <div class="back-name">Mel's Apothecary</div>
  <div class="back-title">Owner/Pharm D</div>

  <ul class="contact-list">
    <li><svg viewBox="0 0 16 16"><path d="M2 5c0-2 2-3 6-3s6 1 6 3v2h-3V5H5v2H2zM4 8h8l2 6H2z"/></svg>605-318-6207</li>
    <li><svg viewBox="0 0 16 16"><path d="M4 1h8v4H4zM1 6h14v6h-3v-2H4v2H1zM5 11h6v4H5z"/></svg>605-318-6209</li>
    <li><svg viewBox="0 0 16 16"><path d="M8 1a7 7 0 1 0 0 14A7 7 0 0 0 8 1zm0 1.5c.8 0 1.6 1.7 1.9 4H6.1C6.4 4.2 7.2 2.5 8 2.5zM2.6 7.5h2.1c0 .3 0 1 .1 1.5H2.6a5 5 0 0 1 0-1.5zm3.5 1.5a9 9 0 0 1 0-1.5h3.8a9 9 0 0 1 0 1.5zm5.2 0c.1-.5.1-1.2.1-1.5h2.1a5 5 0 0 1 0 1.5zM8 13.5c-.8 0-1.6-1.7-1.9-4h3.8c-.3 2.3-1.1 4-1.9 4z"/></svg>melsapothecary-example.com</li>
    <li><svg viewBox="0 0 16 16"><path d="M1 3h14v10H1zm1.5 1.5v.3L8 9l5.5-4.2v-.3zm0 2.2v4.8h11V6.7L8 11z"/></svg>mel@melsapothecary-example.com</li>
    <li class="contact-address">7134 North Brook Lane Sioux Falls, SD 57231</li>
  </ul>

  <div class="lockup">
    <div class="lockup-dot"></div>
    <div class="lockup-rule"></div>
    <div class="lockup-name">Mel's Apothecary</div>
  </div>
</section>

</body>
</html>
```